Bloom Where You Stand redesign book cover

A new cover for my already published book. The old cover looks great but not for a women’s self help book. Cover is killing sales. Once I explain the book it sells quickly AND gets 5 star reviews. Outside of actually explaining the book the cover scares people away. I need a new cover. ASAP! Before The yr end please.
The tag line -
Discover 10 Practical Ways To Replace negative thoughts with knowing the voice of God. This is a self help book for women 35-45 Christian but not religious. Each chapter is a hands on spiritual experience where the reader takes small tests about themselves, discover why they have negative thoughts, what they are and how to listen to God through hands on methods of listening. NOT strange type of things. They learn what 4 voices they are listening to and how to hone in on Jesus voice. There are scriptures to pray and journaling assignments. The old cover is in the brief with the write up for the back of the book. Please use the new author picture, Publishers logo (tree), barcode, and contact info from the back of the book. And yes the author name and title of the book on the spine. Lay out on the back cover needs to be interesting. You have all the info have fun with it.

Target Market(s)

Women 35-45 yrs old Christian and new believers or seekers.

Industry/Entity Type

Non profit organization. Missionary

Requirements
Must have
• Something DIFFERENT than what is there now. Something inviting. Fresh clear title
Nice to have
• Multi colors however a white stand out cover is also good.
Should not have
• Heavy religious feeling. No church steeples, Jesus faces.

```html
<!DOCTYPE html>
<html lang="en">
<head>
<meta charset="utf-8">
<title>Bloom Where You Stand — Book Cover</title>
<link rel="stylesheet" href="https://fonts.googleapis.com/css2?family=Barlow+Condensed:wght@500;600;700&display=swap">
<style>
  :root {
    --page-bg: #eceef0;
    --cover-white: #ffffff;
    --author-blue: #5d7594;
    --water-light: #a9d2ec;
    --water-mid: #3d8fc6;
    --water-deep: #0d6cb0;
    --water-dark: #1b4f80;
    --mist: #dfe4ea;
    --tagline: #ffffff;
  }
  * { margin: 0; padding: 0; box-sizing: border-box; }
  html, body {
    width: 1200px;
    height: 1000px;
    overflow: hidden;
    background: var(--page-bg);
  }
  .stage {
    width: 1200px;
    height: 1000px;
    display: flex;
    align-items: center;
    justify-content: center;
  }
  .book-cover {
    position: relative;
    width: 690px;
    height: 920px;
    background: var(--cover-white);
    overflow: hidden;
    box-shadow: 0 6px 24px rgba(0, 0, 0, 0.12);
    font-family: "Barlow Condensed", "Arial Narrow", sans-serif;
  }
  .cover-photo {
    position: absolute;
    left: 0;
    right: 0;
    top: 380px;
    bottom: 0;
    background:
      linear-gradient(180deg,
        rgba(255,255,255,1) 0%,
        var(--mist) 14%,
        #c9d2dc 28%,
        var(--water-light) 42%,
        var(--water-mid) 52%,
        var(--water-deep) 66%,
        #1a78bb 82%,
        var(--water-deep) 100%);
  }
  .author-name {
    position: absolute;
    top: 38px;
    left: 0;
    right: 0;
    text-align: center;
    color: var(--author-blue);
    font-weight: 500;
    font-size: 46px;
    letter-spacing: 0.12em;
    text-transform: uppercase;
  }
  .book-title {
    position: absolute;
    top: 118px;
    left: 0;
    right: 0;
    text-align: center;
    text-transform: uppercase;
    font-weight: 700;
    font-size: 136px;
    line-height: 0.92;
    letter-spacing: 0.01em;
    background: linear-gradient(180deg, #9cc6e4 0%, #3f86bd 35%, #1d5f97 55%, #6fa9d4 75%, #2f74ad 100%);
    -webkit-background-clip: text;
    background-clip: text;
    color: transparent;
  }
  .book-title .title-line { display: block; }
  .tagline {
    position: absolute;
    left: 0;
    right: 0;
    bottom: 46px;
    text-align: center;
    color: var(--tagline);
    text-transform: uppercase;
    font-weight: 600;
    font-size: 27px;
    line-height: 1.3;
    letter-spacing: 0.02em;
  }
</style>
</head>
<body>
  <main class="stage">
    <article class="book-cover">
      <div class="cover-photo" role="img" aria-label="Photograph of a woman in white floating on her back, head tilted into clear blue water"></div>
      <p class="author-name">Mara Ellison</p>
      <h1 class="book-title">
        <span class="title-line">Bloom Where</span>
        <span class="title-line">You Stand</span>
      </h1>
      <p class="tagline">
        Discover 10 practical ways to replace<br>
        negative thoughts with knowing<br>
        the voice of God
      </p>
    </article>
  </main>
</body>
</html>
```